Microsoft Word Template for 1, 2, and 4-page quick hit, topical pieces

I am looking for someone to create a professional and dynamic Microsoft Word Template that will allow us to easily add content to produce brochures and whitepapers on various topics. We'd like the template to be 4 pages with the idea that we may use all or just 1-2 of the pages in a brochure. We are fond of bold color, white space, and a good ratio of text to graphics. We have a large catalog of stock images so placeholders for photographs can be included if it fits the design. There is the possibility of expanded design opportunities in the future. I have attached our logo and colors.

Target Market(s)

Libraries - Public, Government, Higher Education, and Corporate

Font styles to use
Serif
Sans Serif

Requirements
Must have
• Editable Word Template that has 4 variable but cohesively designed pages. Use our logo and colors (see uploaded documents)
Nice to have
• Lots of white space, spaces for photos and graphics, spaces for blocks of text. Color.
Should not have
• Giant blocks of text. The exact same frame (header and footer) on each page.

```html
<!DOCTYPE html>
<html lang="en">
<head>
<meta charset="utf-8">
<title>Bookwell brochure template pages</title>
<link href="https://fonts.googleapis.com/css2?family=Montserrat:wght@600;700;800&family=Open+Sans:ital,wght@0,300;0,400;0,600;0,700;1,600&display=swap" rel="stylesheet">
<style>
:root{
  --teal:#1f7f92;
  --teal-light:#5eb1bd;
  --green:#6aac43;
  --green-dark:#5a9a36;
  --ink:#4a4a4a;
  --muted:#6b6b6b;
  --brand:#7a6a58;
  --paper:#ffffff;
  --stage:#f1f2f2;
}
*{box-sizing:border-box;margin:0;padding:0}
html,body{width:1200px;height:3000px;overflow:hidden;background:var(--stage)}
body{font-family:"Open Sans",Arial,sans-serif;color:var(--ink);position:relative}
.page{position:absolute;width:336px;height:435px;background:var(--paper);overflow:hidden;box-shadow:0 4px 14px rgba(0,0,0,.12)}
.abs{position:absolute}
.photo{position:absolute}
.photo-desk{background:linear-gradient(135deg,#d9dcdd 0%,#9aa3a8 45%,#4f5a62 100%)}
.photo-laptop{background:linear-gradient(160deg,#eef0f0 0%,#c4c9cc 50%,#6b7177 100%)}
.photo-office{background:linear-gradient(120deg,#c9cfd2 0%,#7f8b92 55%,#3c444b 100%)}
.photo-warm{background:linear-gradient(140deg,#e6e1da 0%,#b9aa98 50%,#6f6456 100%)}
.photo-dark{background:linear-gradient(150deg,#5b6670 0%,#2f363c 100%)}
.hd{font-family:"Montserrat",Arial,sans-serif;font-weight:700;font-size:10.5px;color:var(--green)}
.hd-teal{color:var(--teal)}
.sub{font-family:"Montserrat",Arial,sans-serif;font-weight:700;font-size:6px}
.copy{font-size:5.1px;line-height:1.5;color:var(--muted)}
.copy-teal{color:var(--teal)}
.copy-white{color:#fff}
.copy p+p{margin-top:4px}
.mini-hd{font-family:"Montserrat",Arial,sans-serif;font-weight:700;font-size:5.6px;color:var(--green);border-bottom:.8px solid var(--green);padding-bottom:2px;margin-bottom:3px}
.caption-bar{position:absolute;background:var(--green);color:#fff;font-weight:600;font-size:6px;padding:3px 8px}
.brand{position:absolute;display:flex;align-items:center;gap:5px;font-family:"Open Sans",Arial,sans-serif;font-weight:300;color:var(--brand)}
.brand-dot{border-radius:50%;background:var(--green)}
.bullets{list-style:none;font-size:5.2px;color:var(--ink);line-height:1.7}
.bullets li::before{content:"»";color:var(--green);font-weight:700;margin-right:5px}
.num{width:17px;height:17px;border-radius:50%;background:var(--green);color:#fff;font-family:"Montserrat",Arial,sans-serif;font-weight:700;font-size:7px;display:flex;align-items:center;justify-content:center;margin-bottom:4px}
.thumb-label{font-family:"Montserrat",Arial,sans-serif;font-weight:700;font-size:5px;color:var(--green);margin-bottom:3px}
.contact{list-style:none;font-size:5px;color:var(--teal);line-height:2.1}
.contact li{display:flex;align-items:center;gap:5px}
.contact svg{width:7px;height:7px;flex:none}
</style>
</head>
<body>

<!-- Row 1 -->
<section class="page page-cover" style="left:66px;top:808px">
  <div class="abs" style="left:0;top:0;width:29px;height:241px;background:var(--teal)"></div>
  <div class="photo photo-laptop" style="left:29px;top:0;width:307px;height:241px" role="img" aria-label="Photo of hands typing on a laptop on a wooden desk"></div>
  <h1 class="abs" style="left:35px;top:252px;font-family:'Montserrat',Arial,sans-serif;font-weight:700;font-size:19px;color:var(--green)">SOME TEXT HERE</h1>
  <p class="abs" style="left:35px;top:275px;font-size:13px;font-weight:400;color:var(--green)">some text here</p>
  <div class="abs copy" style="left:35px;top:298px;width:255px">
    <p>Lorem ipsum dolor sit amet, consectetuer adipiscing elit. Maecenas porttitor congue massa. Fusce posuere, magna sed pulvinar ultricies, purus lectus malesuada libero, sit amet commodo magna eros quis urna.</p>
    <p>Aenean nec lorem. In porttitor. Donec laoreet nonummy augue.</p>
    <p>Suspendisse dui purus, scelerisque at, vulputate vitae, pretium mattis, nunc. Mauris eget neque at sem venenatis eleifend. Ut nonummy.</p>
  </div>
  <div class="brand" style="left:36px;top:368px;font-size:22px"><span class="brand-dot" style="width:22px;height:22px"></span>Bookwell</div>
  <div class="abs" style="left:0;bottom:0;width:336px;height:8px;background:var(--green)"></div>
</section>

<section class="page page-intro" style="left:432px;top:808px">
  <h2 class="abs hd" style="left:24px;top:18px">Header Text</h2>
  <div class="abs copy" style="left:24px;top:36px;width:142px">
    <p>Lorem ipsum dolor sit amet, consectetuer adipiscing elit. Maecenas porttitor congue massa. Fusce posuere, magna sed pulvinar ultricies, purus lectus malesuada libero, sit amet commodo magna eros quis urna. adipiscing elit. Maecenas porttitor congue massa. Fusce posuere, magna sed pulvinar ultricies, purus lectus malesuada libero, sit amet commodo magna eros quis urna.</p>
  </div>
  <h3 class="abs sub" style="left:184px;top:21px;color:var(--teal);font-size:5.6px">LOREM IPSUM DOLOR SIT AMET</h3>
  <ul class="abs bullets" style="left:193px;top:33px">
    <li>Lorem Ipsum Dolor</li><li>Lorem Ipsum Dolor</li><li>Lorem Ipsum Dolor</li><li>Lorem Ipsum Dolor</li><li>Lorem Ipsum Dolor</li>
  </ul>
  <div class="photo photo-dark" style="left:24px;top:105px;width:142px;height:108px" role="img" aria-label="Photo of hands on a laptop showing code"></div>
  <div class="abs copy copy-white" style="left:24px;top:213px;width:142px;height:15px;background:var(--green);padding:2px 8px;text-align:center">Lorem ipsum dolor sit amet, consectetuer adipiscing elit. Maecenas porttitor</div>
  <div class="abs copy copy-teal" style="left:187px;top:103px;width:128px">
    <p>Lorem ipsum dolor sit amet, consectetuer adipiscing elit. Maecenas porttitor congue massa. Fusce posuere, magna sed pulvinar ultricies, purus lectus malesuada libero, sit amet commodo magna eros quis urna.</p>
    <p>adipiscing elit. Maecenas porttitor congue massa. Fusce posuere, magna sed pulvinar ultricies, purus lectus malesuada libero, sit amet commodo magna eros quis urna.</p>
    <p>Lorem ipsum dolor sit amet, consectetuer adipiscing elit. Maecenas porttitor congue massa. Fusce posuere, magna sed pulvinar ultricies, purus lectus malesuada libero, sit amet commodo magna eros quis urna.</p>
    <p>adipiscing elit. Maecenas porttitor congue massa. Fusce posuere, magna sed pulvinar ultricies, commodo magna eros quis urna.</p>
  </div>
  <h2 class="abs hd" style="left:24px;top:244px">Header Text</h2>
  <div class="abs copy" style="left:24px;top:262px;width:290px">
    <p>Lorem ipsum dolor sit amet, consectetuer adipiscing elit. Maecenas porttitor congue massa. Fusce posuere, magna sed pulvinar ultricies, purus lectus malesuada libero, sit amet commodo magna eros quis urna.</p>
  </div>
  <div class="abs" style="left:24px;top:287px;display:flex;gap:20px">
    <figure style="width:58px"><div class="thumb-label">Image 1</div><div style="height:55px" class="photo-laptop" role="img" aria-label="Photo of a laptop keyboard"></div><figcaption class="copy" style="margin-top:3px">porttitor congue massa. Fusce sed malesuada libero,</figcaption></figure>
    <figure style="width:58px"><div class="thumb-label">Image 2</div><div style="height:55px" class="photo-laptop" role="img" aria-label="Photo of a laptop keyboard"></div><figcaption class="copy" style="margin-top:3px">porttitor congue massa. Fusce sed malesuada libero,</figcaption></figure>
    <figure style="width:58px"><div class="thumb-label">Image 3</div><div style="height:55px" class="photo-laptop" role="img" aria-label="Photo of a laptop keyboard"></div><figcaption class="copy" style="margin-top:3px">porttitor congue massa. Fusce sed malesuada libero,</figcaption></figure>
    <figure style="width:58px"><div class="thumb-label">Image 4</div><div style="height:55px" class="photo-laptop" role="img" aria-label="Photo of a laptop keyboard"></div><figcaption class="copy" style="margin-top:3px">porttitor congue massa. Fusce sed malesuada libero,</figcaption></figure>
  </div>
</section>

<section class="page page-steps" style="left:798px;top:808px">
  <h2 class="abs hd" style="left:24px;top:21px">Header Text</h2>
  <div class="abs copy" style="left:24px;top:40px;width:118px">
    <p>Lorem ipsum dolor sit amet, consectetuer adipiscing elit. Maecenas porttitor congue massa. Fusce posuere, magna sed pulvinar ultricies, purus lectus malesuada libero, sit amet commodo magna eros quis urna. adipiscing elit. Maecenas porttitor congue massa. Fusce posuere, magna sed pulvinar ultricies, purus lectus malesuada libero, sit amet commodo magna eros quis urna.</p>
    <p>Lorem ipsum dolor sit amet, consectetuer adipiscing elit. Maecenas porttitor congue massa. Fusce posuere, magna sed pulvinar ultricies, purus lectus malesuada libero, sit amet commodo magna eros quis urna. adipiscing elit. Maecenas porttitor congue massa. Fusce posuere, magna</p>
  </div>
  <div class="abs" style="left:145px;top:0;width:191px;height:20px;background:var(--green)"></div>
  <div class="photo photo-office" style="left:145px;top:20px;width:191px;height:180px" role="img" aria-label="Photo of a man working at a desktop computer in an office"></div>
  <div class="abs" style="left:24px;top:209px;width:290px;display:grid;grid-template-columns:1fr 1fr;column-gap:24px;row-gap:14px">
    <div><div class="num">1</div><div class="mini-hd">Header Text</div><p class="copy">Lorem ipsum dolor sit amet, consectetuer adipiscing elit. Maecenas porttitor congue massa. Fusce posuere, magna sed pulvinar ultricies, purus lectus malesuada libero, sit amet commodo magna eros quis urna. adipiscing elit. Maecenas porttitor</p></div>
    <div><div class="num">2</div><div class="mini-hd">Header Text</div><p class="copy">Lorem ipsum dolor sit amet, consectetuer adipiscing elit. Maecenas porttitor congue massa. Fusce posuere, magna sed pulvinar ultricies, purus lectus malesuada libero, sit amet commodo magna eros quis urna. adipiscing elit. Maecenas porttitor</p></div>
    <div><div class="num">3</div><div class="mini-hd">Header Text</div><p class="copy">Lorem ipsum dolor sit amet, consectetuer adipiscing elit. Maecenas porttitor congue massa. Fusce posuere, magna sed pulvinar ultricies, purus lectus malesuada libero, sit amet commodo magna eros quis urna. adipiscing elit. Maecenas porttitor</p></div>
    <div><div class="num">4</div><div class="mini-hd">Header Text</div><p class="copy">Lorem ipsum dolor sit amet, consectetuer adipiscing elit. Maecenas porttitor congue massa. Fusce posuere, magna sed pulvinar ultricies, purus lectus malesuada libero, sit amet commodo magna eros quis urna. adipiscing elit. Maecenas porttitor</p></div>
  </div>
</section>

<!-- Row 2 -->
<section class="page page-feature" style="left:66px;top:1283px">
  <h2 class="abs hd" style="left:24px;top:20px">Header Text</h2>
  <div class="abs copy" style="left:24px;top:38px;width:290px">
    <p>Lorem ipsum dolor sit amet, consectetuer adipiscing elit. Maecenas porttitor congue massa. Fusce posuere, magna sed pulvinar ultricies, purus lectus malesuada libero, sit amet commodo magna eros quis urna. adipiscing elit. Maecenas porttitor congue massa. Fusce posuere, magna sed pulvinar</p>
  </div>
  <div class="photo photo-warm" style="left:24px;top:76px;width:167px;height:160px" role="img" aria-label="Photo of a person working on a laptop beside a stack of books"></div>
  <div class="abs" style="left:191px;top:76px;width:127px;height:160px;background:var(--green);padding:7px 8px">
    <h3 style="font-family:'Montserrat',Arial,sans-serif;font-weight:700;font-size:8px;color:#fff;margin-bottom:5px">Lorem ipsum dolor</h3>
    <div class="copy copy-white">
      <p>sit amet, consectetuer adipiscing elit. Maecenas porttitor congue massa. Fusce posuere, magna sed pulvinar ultricies, purus lectus malesuada libero, sit amet commodo magna eros quis urna. adipiscing elit. Maecenas porttitor congue massa. Fusce posuere, magna sed pulvinar ultricies, purus lectus malesuada libero, sit amet commodo magna eros quis urna.</p>
      <p>Lorem ipsum dolor sit amet, consectetuer adipiscing elit. Maecenas porttitor congue massa. Fusce posuere, magna sed pulvinar ultricies, purus lectus malesuada libero, sit amet commodo magna eros quis urna.</p>
    </div>
  </div>
  <div class="abs" style="left:24px;top:246px;width:290px;display:grid;grid-template-columns:repeat(3,1fr);gap:10px">
    <div><h4 class="sub" style="color:var(--teal);margin-bottom:3px">Lorem ipsum dolor</h4><div class="copy"><p>sit amet, consectetuer adipiscing elit. Maecenas porttitor congue massa. Fusce posuere, magna sed pulvinar ultricies, purus lectus malesuada libero, sit amet commodo magna eros quis urna. adipiscing elit. Maecenas porttitor congue massa. Fusce magna eros quis urna.</p><p>Lorem ipsum dolor sit amet, consectetuer adipiscing elit. Maecenas porttitor congue massa. Fusce posuere, magna sed pulvinar ultricies, purus lectus adipiscing elit. Maecenas porttitor</p></div></div>
    <div><h4 class="sub" style="color:var(--teal);margin-bottom:3px">Lorem ipsum dolor</h4><div class="copy"><p>sit amet, consectetuer adipiscing elit. Maecenas porttitor congue massa. Fusce posuere, magna sed pulvinar ultricies, purus lectus malesuada libero, sit amet commodo magna eros quis urna. adipiscing elit. Maecenas porttitor congue massa. Fusce posuere, magna sed pulvinar ultricies, purus lectus malesuada libero, sit amet commodo magna eros quis urna.</p><p>lectus adipiscing elit. Maecenas porttitor</p></div></div>
    <div><h4 class="sub" style="color:var(--teal);margin-bottom:3px">Lorem ipsum dolor</h4><div class="copy"><p>sit amet, consectetuer adipiscing elit. Maecenas porttitor congue massa. Fusce posuere, magna sed pulvinar ultricies, purus lectus malesuada libero, sit amet commodo magna eros quis urna. adipiscing elit. Maecenas porttitor congue massa. Fusce posuere, magna sed pulvinar ultricies, purus lectus malesuada libero, sit amet commodo magna eros quis urna.</p><p>Lorem ipsum dolor sit amet, consectetuer adipiscing elit. Maecenas porttitor congue massa. Fusce posuere, magna</p></div></div>
  </div>
</section>

<section class="page page-story" style="left:432px;top:1283px">
  <h2 class="abs hd" style="left:24px;top:20px">Header Text</h2>
  <div class="photo photo-office" style="left:24px;top:42px;width:294px;height:118px" role="img" aria-label="Photo of people working at laptops in a bright office"></div>
  <div class="caption-bar" style="left:24px;top:150px;width:294px;height:17px">Lorem ipsum dolor</div>
  <div class="abs" style="left:24px;top:175px;width:294px">
    <div class="mini-hd" style="font-size:5px">Lorem ipsum dolor</div>
    <div class="copy"><p>sit amet, consectetuer adipiscing elit. Maecenas porttitor congue massa. Fusce posuere, magna sed pulvinar ultricies, purus lectus malesuada libero, sit amet commodo magna eros quis urna. adipiscing elit. Maecenas porttitor congue massa. Fusce magna eros quis urna.</p><p>Lorem ipsum dolor sit amet, consectetuer adipiscing elit. Maecenas porttitor congue massa. Fusce posuere, magna sed pulvinar ultricies, purus lectus adipiscing elit. Maecenas porttitor</p></div>
  </div>
  <div class="photo photo-laptop" style="left:24px;top:240px;width:70px;height:64px" role="img" aria-label="Photo of a laptop on a desk"></div>
  <div class="abs" style="left:103px;top:241px;width:215px">
    <h4 class="sub" style="color:var(--teal);font-size:5.2px">Lorem ipsum dolor</h4>
    <div class="copy"><p>sit amet, consectetuer adipiscing elit. Maecenas porttitor congue massa. Fusce posuere, magna sed pulvinar ultricies, purus lectus malesuada libero, sit amet commodo magna eros quis urna. adipiscing elit. Maecenas porttitor congue massa. Fusce magna eros quis urna.</p><p>Lorem ipsum dolor sit amet, consectetuer adipiscing elit. Maecenas porttitor congue massa. Fusce posuere, magna sed pulvinar ultricies, purus lectus adipiscing elit. Maecenas porttitor</p></div>
  </div>
  <div class="photo photo-laptop" style="left:24px;top:317px;width:70px;height:64px" role="img" aria-label="Photo of a laptop on a desk"></div>
  <div class="abs" style="left:103px;top:318px;width:215px">
    <h4 class="sub" style="color:var(--teal);font-size:5.2px">Lorem ipsum dolor</h4>
    <div class="copy"><p>sit amet, consectetuer adipiscing elit. Maecenas porttitor congue massa. Fusce posuere, magna sed pulvinar ultricies, purus lectus malesuada libero, sit amet commodo magna eros quis urna. adipiscing elit. Maecenas porttitor congue massa. Fusce magna eros quis urna.</p><p>Lorem ipsum dolor sit amet, consectetuer adipiscing elit. Maecenas porttitor congue massa. Fusce posuere, magna sed pulvinar ultricies, purus lectus adipiscing elit. Maecenas porttitor</p></div>
  </div>
</section>

<section class="page page-article" style="left:798px;top:1283px">
  <h2 class="abs hd hd-teal" style="left:24px;top:20px">Header Text</h2>
  <p class="abs" style="left:24px;top:36px;font-size:6px;font-weight:600;font-style:italic;color:var(--teal)">lectus adipiscing elit. Maecenas porttitor</p>
  <h3 class="abs sub" style="left:24px;top:54px;color:var(--teal)">Lorem ipsum dolor</h3>
  <div class="abs copy" style="left:24px;top:64px;width:122px">
    <p>sit amet, consectetuer adipiscing elit. Maecenas porttitor congue massa. Fusce posuere, magna sed pulvinar ultricies, purus lectus malesuada libero, sit amet commodo magna eros quis urna. adipiscing elit. Maecenas porttitor congue massa. Fusce magna eros quis urna.</p>
    <p>Lorem ipsum dolor sit amet, consectetuer adipiscing elit. Maecenas porttitor congue massa. Fusce posuere, magna sed pulvinar ultricies, purus lectus adipiscing elit. Maecenas porttitor sit amet consectetuer adipiscing elit. Maecenas porttitor congue massa. Fusce posuere, magna sed pulvinar ultricies, purus lectus malesuada libero, sit amet commodo magna eros quis urna. adipiscing elit. Maecenas porttitor congue massa.</p>
    <p>Lorem ipsum dolor sit amet, consectetuer adipiscing elit. Maecenas porttitor congue massa. Fusce posuere, magna sed pulvinar ultricies, purus lectus adipiscing elit. Maecenas porttitor congue massa. Fusce posuere, magna sed pulvinar ultricies, purus lectus malesuada libero, sit amet commodo magna eros quis urna.</p>
    <p>Lorem ipsum dolor sit amet, consectetuer adipiscing elit. Maecenas porttitor congue massa. Fusce posuere, magna sed pulvinar ultricies, purus lectus adipiscing elit. Maecenas porttitor</p>
    <p>Lorem ipsum dolor sit amet, consectetuer adipiscing elit. Maecenas porttitor congue massa. Fusce posuere, magna sed pulvinar ultricies, purus lectus adipiscing elit. Maecenas porttitor</p>
  </div>
  <div class="photo photo-desk" style="left:157px;top:57px;width:179px;height:338px" role="img" aria-label="Photo of a person sketching plans beside a laptop"></div>
</section>

<!-- Row 3 -->
<section class="page page-back" style="left:432px;top:1758px">
  <div class="photo photo-dark" style="left:0;top:0;width:306px;height:290px" role="img" aria-label="Photo of a person holding a phone and coffee beside a laptop"></div>
  <div class="abs" style="left:306px;top:0;width:30px;height:256px;background:var(--teal)"></div>
  <div class="abs" style="left:0;top:171px;width:168px;height:224px;background:var(--teal-light);opacity:.92"></div>
  <h2 class="abs" style="left:23px;top:181px;font-family:'Montserrat',Arial,sans-serif;font-weight:700;font-size:17px;line-height:1.3;color:#fff">Some text<br>here</h2>
  <div class="abs copy copy-white" style="left:23px;top:259px;width:130px">
    <p>Lorem ipsum dolor sit amet, consectetuer adipiscing elit. Maecenas porttitor congue massa. Fusce posuere, magna sed pulvinar ultricies, purus lectus malesuada libero, sit amet commodo magna eros quis urna.</p>
    <p style="margin-top:12px">Lorem ipsum dolor sit amet, consectetuer adipiscing elit. Maecenas porttitor congue massa. Fusce posuere, magna sed pulvinar ultricies, purus lectus malesuada libero, sit amet commodo magna eros quis urna.</p>
  </div>
  <div class="abs copy copy-teal" style="left:185px;top:257px;width:128px">
    <p>Lorem ipsum dolor sit amet, consectetuer adipiscing elit. Maecenas porttitor congue massa. Fusce posuere, magna sed pulvinar ultricies, purus lectus malesuada libero, sit amet commodo magna eros quis urna.</p>
    <p>Lorem ipsum dolor sit amet, consectetuer adipiscing elit. Maecenas porttitor congue massa. Fusce posuere, magna sed pulvinar ultricies, purus lectus malesuada libero, sit.</p>
  </div>
  <div class="brand" style="left:24px;top:402px;font-size:17px"><span class="brand-dot" style="width:16px;height:16px"></span>Bookwell</div>
  <ul class="abs contact" style="left:215px;top:372px">
    <li><svg viewBox="0 0 10 10"><circle cx="5" cy="5" r="5" fill="#6aac43"/><path d="M3.4 2.6c.3-.3.7-.2.9.1l.5.8c.1.3 0 .5-.2.7l-.3.2c.3.7.8 1.2 1.5 1.5l.2-.3c.2-.2.4-.3.7-.2l.8.5c.3.2.4.6.1.9l-.4.4C6.5 7.9 2.1 3.5 3 3z" fill="#fff"/></svg>+100 555 0199</li>
    <li><svg viewBox="0 0 10 10"><circle cx="5" cy="5" r="5" fill="#6aac43"/><rect x="2.6" y="3.3" width="4.8" height="3.4" fill="none" stroke="#fff" stroke-width=".7"/><path d="M2.6 3.3 5 5.2l2.4-1.9" fill="none" stroke="#fff" stroke-width=".7"/></svg>hello@bookwell.example</li>
    <li><svg viewBox="0 0 10 10"><circle cx="5" cy="5" r="5" fill="#6aac43"/><circle cx="5" cy="5" r="2.5" fill="none" stroke="#fff" stroke-width=".6"/><path d="M2.5 5h5M5 2.5c-1.2 1.4-1.2 3.6 0 5M5 2.5c1.2 1.4 1.2 3.6 0 5" fill="none" stroke="#fff" stroke-width=".5"/></svg>www.bookwell.example</li>
    <li><svg viewBox="0 0 10 10"><circle cx="5" cy="5" r="5" fill="#6aac43"/><path d="M5 8 3.2 5.3a2 2 0 1 1 3.6 0z" fill="#fff"/><circle cx="5" cy="4.3" r=".7" fill="#6aac43"/></svg>your address here</li>
  </ul>
</section>

</body>
</html>
```